Flyer for a marketing

We are a holistic mental health facility in need of a flyer to help promote our services and encourage more people to seek care. See the attachment to tell you more. We prefer warm green colors or rich blue. Thank you.

```html
<!DOCTYPE html>
<html lang="en">
<head>
<meta charset="utf-8">
<title>Haven Mind Health and Wellness – Flyer</title>
<link href="https://fonts.googleapis.com/css2?family=Montserrat:ital,wght@0,400;0,500;0,600;0,700;0,800;1,800&display=swap" rel="stylesheet">
<style>
  :root{
    --backdrop:#a7c4c6;
    --paper:#ffffff;
    --navy:#1d3f66;
    --cyan:#3ec3ea;
    --band-light:#a1e2f5;
    --band-mid:#2e7ea6;
    --img-deep:#23406a;
    --img-mid:#2f7fd6;
    --img-soft:#bfe3f2;
  }
  *{margin:0;padding:0;box-sizing:border-box}
  html,body{width:1008px;height:1200px;overflow:hidden;background:var(--backdrop)}
  body{font-family:"Montserrat",Arial,sans-serif;color:var(--navy);position:relative}
  .flyer{position:absolute;left:166px;top:123px;width:675px;height:954px;background:var(--paper);overflow:hidden}
  .brand{position:absolute;left:54px;top:50px;display:flex;align-items:center;gap:14px}
  .brand-mark{width:16px;height:16px;background:var(--cyan)}
  .brand-name{font-weight:600;font-size:13px;line-height:19px;letter-spacing:.06em;text-transform:uppercase;color:var(--navy);border-left:2px solid var(--navy);padding-left:14px}
  .tagline{position:absolute;left:65px;top:160px;font-size:18px;font-weight:400;letter-spacing:.03em;color:var(--navy)}
  .hero-visual{position:absolute;left:302px;top:34px;width:333px;height:235px;border-radius:28px;
    background:linear-gradient(135deg,var(--img-deep) 0%,var(--img-mid) 45%,var(--img-soft) 100%)}
  .headline{position:absolute;left:52px;top:214px;font-weight:800;font-size:55px;line-height:63px;color:var(--navy);letter-spacing:-.01em}
  .subhead{position:absolute;left:53px;top:412px;font-weight:800;font-size:31px;line-height:37px;color:var(--cyan)}
  .availability{position:absolute;left:0;width:100%;top:506px;text-align:center;font-weight:800;font-style:italic;font-size:26px;line-height:32px;color:var(--navy)}
  .call-prompt{position:absolute;left:0;width:100%;top:585px;text-align:center;font-size:16.8px;font-weight:500;line-height:27px}
  .call-prompt strong{font-size:25px;font-weight:800;margin-right:4px}
  .why{position:absolute;left:0;width:100%;top:664px;text-align:center;font-size:12.5px;line-height:15.5px;font-weight:500}
  .why h2{font-size:12.5px;font-weight:800;margin-bottom:2px}
  .promise{position:absolute;left:0;width:100%;top:766px;text-align:center;font-size:11.5px;line-height:14px;font-weight:700}
  .band-light{position:absolute;left:0;top:806px;width:100%;height:10px;background:var(--band-light)}
  .band-mid{position:absolute;left:0;top:816px;width:100%;height:10px;background:var(--band-mid)}
  .footer{position:absolute;left:0;top:826px;width:100%;height:128px;background:var(--navy);color:#fff}
  .footer .divider{position:absolute;left:291px;top:3px;width:2px;height:111px;background:#fff}
  .contact-line{position:absolute;display:flex;align-items:center;gap:12px;font-weight:700}
  .contact-line svg{flex:none}
  .phone{left:37px;top:33px;font-size:18.5px}
  .fax{left:37px;top:77px;font-size:18.5px}
  .address{left:307px;top:18px;font-size:10.5px;line-height:13px;gap:10px}
  .email{left:308px;top:54px;font-size:16px;gap:9px}
  .web{left:308px;top:81px;font-size:16px;gap:9px}
</style>
</head>
<body>
<main class="flyer">
  <div class="brand">
    <span class="brand-mark"></span>
    <div class="brand-name">Haven<br>Mind<br>Health<br>and<br>Wellness</div>
  </div>
  <p class="tagline">The Care You Deserve</p>

  <div class="hero-visual" role="img" aria-label="Photo collage: a person sitting alone in a hallway, a glowing brain, and a head profile with puzzle pieces"></div>

  <h1 class="headline">Haven<br>Mind Health<br>and Wellness,</h1>
  <p class="subhead">where deserving patients meet<br>compassionate providers.</p>

  <p class="availability">We are accepting new patients,<br>no waiting list.</p>

  <p class="call-prompt">Your mental health matters, so make it a priority and<br><strong>call us today</strong> for an appointment.</p>

  <section class="why">
    <h2>Why choose us?</h2>
    <p>We are an integrative holistic psychiatric center.<br>
    Our mission is to provide compassionate quality care.<br>
    We provide psychiatric services including medication<br>
    management and psychotherapy.</p>
  </section>

  <p class="promise">We listen, care, and empower you to live better.<br>We accept major insurances.</p>

  <div class="band-light"></div>
  <div class="band-mid"></div>

  <footer class="footer">
    <div class="divider"></div>
    <div class="contact-line phone">
      <svg width="24" height="24" viewBox="0 0 24 24" fill="none" stroke="#fff" stroke-width="1.6"><circle cx="12" cy="12" r="10.5"/><path d="M8.3 6.8l1.6-.3 1.1 2.6-1.1 1c.6 1.4 1.6 2.5 3 3.1l1-1.1 2.6 1.1-.3 1.6c-3.8.5-8.4-4.1-7.9-8z" fill="#fff" stroke-width="1"/></svg>
      <span>Ph (555) 014-2290</span>
    </div>
    <div class="contact-line fax">
      <svg width="24" height="22" viewBox="0 0 24 22" fill="#fff"><rect x="6" y="1" width="12" height="6" rx="1"/><rect x="1" y="7" width="22" height="10" rx="2"/><rect x="6" y="13" width="12" height="8" rx="1" fill="#fff" stroke="#1d3f66" stroke-width="1.5"/><rect x="8.5" y="16" width="7" height="1.2" fill="#1d3f66"/></svg>
      <span>Fax (555) 018-4471</span>
    </div>
    <div class="contact-line address">
      <svg width="16" height="22" viewBox="0 0 16 22"><path d="M8 1a7 7 0 0 0-7 7c0 5 7 13 7 13s7-8 7-13a7 7 0 0 0-7-7z" fill="#fff"/><circle cx="8" cy="8" r="2.6" fill="#1d3f66"/></svg>
      <span>Haven Mind Health and Wellness, APNC<br>1480 Maple Ridge Drive, Suite 200 Springvale, CA 90210</span>
    </div>
    <div class="contact-line email">
      <svg width="17" height="13" viewBox="0 0 17 13" fill="none" stroke="#fff" stroke-width="1.5"><rect x="1" y="1" width="15" height="11" rx="1.5"/><path d="M1.5 2l7 5.5 7-5.5"/></svg>
      <span>hello@havenmindhealth.com</span>
    </div>
    <div class="contact-line web">
      <svg width="16" height="16" viewBox="0 0 16 16" fill="none" stroke="#fff" stroke-width="1.3"><circle cx="8" cy="8" r="7"/><ellipse cx="8" cy="8" rx="3" ry="7"/><path d="M1 8h14M2 4.5h12M2 11.5h12"/></svg>
      <span>havenmindhealth.com</span>
    </div>
  </footer>
</main>
</body>
</html>
```